Commercial Rooftop Solar business needs a website

We need a website with fantastic appeal for a new company based in Melbourne called Quillmark Energy. We design and install solar energy systems for commercial applications across Australia. Our market is to focus on small to medium businesses looking for solar solutions, but we will also provide our service for residential customers. We would like a beautiful 'front page' feel to our home page, using photographs of solar PV systems and/or natural imagery. Our logo uses the colours orange and black, which could easily be echoed in photographic imagery of sunset and sunrise, for example. The design should communicate quiet confidence and professionalism to a corporate marketplace.

NEW POINTS FOR BRIEF: This design also needs to be flexible to allow for additional future content, including a Support page with sub pages, FAQ's, and a Blog.

As part of this design project, we will require the coding for the website to be completed by the designer.

We have seen some websites, which we like the look and feel of: these are listed below.

brindlecourtpower.com.au:

• Beautiful images underlaying brief text selling points.
• Simple ‘front cover’ style home page with elegant drop-down menu, stylish simple font style.
• Home page invites exploration through the menu links, rather than trying to provide all the information up front.
• Company logo and name in the top left hand corner, contact details accessible at top right hand, seems consistent in most sites.

tovaleenergy.com.au

morvickenergy.example:
• Same element as the others is the front-page style home page with beautiful images underlying text.

We have a webpage that we started uploading content to. You can use some of the content there in your designs: www.quillmarkenergy.example.au

Technical Specifications:
PAGES:

Home

About Us

Solutions - Commercial
- Residential

Products - Solar Panels - Ravel Osprey, Ravel DUNE, Ravel QT
- Solar Inverters - Welmoor, VoltaBrim
- Monitoring systems - Grid Ledgerwise
- Batteries - TK

- Datasheets have been provided for reference but if it's too much work, you can use generic text and we will provide content later.

Contact Us

FUTURE PAGES (Please consider in structure, where links could be placed):

Support

FAQ's

Blog.

We could provide some content for the Support page soon, but the Blog and FAQ's are future pages which we don't want highlighted in the design as we don't yet have content.

Phone: 1800 7 BRYND
Email: sales@quillmarkenergy.example.au

Currently, I do not have images and text available. Please
use placeholders in the meantime. The final text and images will be uploaded for the winner once a winning design has been selected.

Target Market(s)

Primary focus is on small to medium sized business owners. Those owners will have a house which may be suitable for solar so we want to cater to residential deeper in the website.

Industry/Entity Type

Solar Energy

Coding

Coded - Design and coding required

Number of Pages Required

5+ page

Colors
f78f20
0255a3

Requirements
Must have
• Logo as per attachments.
Nice to have
• Logo can have alternate colours Eg. White on Orange or Black etc. provided colour correct logo is shown somewhere eg. footer or contact page.
• In the active site, I'd like to have:
• Very slowly zooming images - barely perceptible.
• Title text that rolls into place
• Subtle movements
• See https://pellowfund.example.au/ for example

```html
<!DOCTYPE html>
<html lang="en">
<head>
<meta charset="utf-8">
<title>Quillmark Energy</title>
<link rel="stylesheet" href="https://fonts.googleapis.com/css2?family=Raleway:wght@400;500;600;700;800&display=swap">
<style>
:root{
  --orange:#f15a24;
  --dark:#2b2b2b;
  --darker:#1f1f1f;
  --ink:#222;
  --muted:#666;
  --line:#dedede;
  --white:#fff;
}
*{box-sizing:border-box;margin:0;padding:0}
html,body{width:1200px;height:2885px;overflow:hidden}
body{font-family:'Raleway',Arial,sans-serif;color:var(--ink);background:var(--white)}
.page{position:relative;width:1200px;height:2885px;overflow:hidden}
.abs{position:absolute}

/* top bar */
.topbar{left:0;top:0;width:1200px;height:37px;background:var(--dark);color:#ddd;font-size:12px}
.topbar .item{position:absolute;top:0;height:37px;display:flex;align-items:center;gap:8px;white-space:nowrap}
.topbar .social{right:104px;top:0;height:37px;display:flex;align-items:center;gap:16px}
.dot{width:9px;height:9px;border-radius:50%;background:#ddd;display:block}

/* header */
.header{left:0;top:37px;width:1200px;height:96px;background:var(--white)}
.brand{position:absolute;left:106px;top:26px;display:flex;align-items:center;gap:12px}
.brand-mark{width:44px;height:44px;border-radius:50%;background:var(--orange)}
.brand-name{font-size:28px;font-weight:700;color:var(--ink);letter-spacing:.5px}
.info{position:absolute;top:30px;display:flex;align-items:center;gap:8px;white-space:nowrap}
.info .ring{width:36px;height:36px;border:1.5px solid var(--orange);border-radius:50%;display:flex;align-items:center;justify-content:center;flex:none}
.info .label{font-size:12px;color:var(--orange);font-weight:600;text-transform:uppercase}
.info .value{font-size:12px;color:#333;margin-top:2px}
.info .value b{font-size:13px;font-weight:600}

/* nav */
.nav{left:0;top:133px;width:1200px;height:46px;background:var(--orange)}
.nav ul{list-style:none;display:flex;gap:30px;position:absolute;left:112px;top:0;height:46px;align-items:center}
.nav li{color:var(--white);font-size:13px;font-weight:500}
.quote-btn{position:absolute;left:956px;top:0;width:146px;height:46px;background:var(--dark);color:var(--white);font-size:12.5px;font-weight:600;display:flex;align-items:center;justify-content:center}

/* hero */
.hero{left:0;top:179px;width:1200px;height:513px;background:linear-gradient(160deg,#6f8796 0%,#3f5a78 35%,#23355a 65%,#1b2944 100%)}
.hero h1{position:absolute;left:0;width:1200px;top:186px;text-align:center;color:var(--white);font-size:45px;font-weight:700;line-height:50px;letter-spacing:-.5px}
.btn{display:flex;align-items:center;justify-content:center;font-size:13px;color:var(--white);height:46px}
.hero .btn-primary{position:absolute;left:456px;top:306px;width:124px;background:var(--orange)}
.hero .btn-secondary{position:absolute;left:586px;top:306px;width:122px;background:#333}

/* section titles */
.section-title{left:0;width:1200px;text-align:center;font-size:21px;font-weight:600;color:var(--ink);text-transform:uppercase}
.rule{width:60px;height:2px;background:var(--orange);left:570px}
.section-lead{left:0;width:1200px;text-align:center;font-size:12.5px;line-height:22px;color:var(--muted)}

/* cards */
.card{border:1px solid var(--line);background:var(--white)}
.card .media{width:100%}
.card h3{font-size:16px;font-weight:700;text-transform:uppercase;color:var(--ink);margin:22px 0 0 8px}
.card p{font-size:12px;line-height:20px;color:var(--muted);margin:10px 0 0 8px;width:280px}
.card .more{font-size:12px;font-weight:700;color:var(--orange);text-transform:uppercase;margin:20px 0 0 8px;display:block}

/* about */
.about-media{left:0;top:1294px;width:590px;height:504px;background:linear-gradient(180deg,#6ea7d6 0%,#9cc4e4 45%,#5e7fa8 70%,#2f4d82 100%)}
.about{left:590px;top:1294px;width:610px;height:504px;background:var(--orange);color:var(--white)}
.about h2{position:absolute;left:64px;top:30px;font-size:21px;font-weight:700}
.about .copy{position:absolute;left:64px;top:96px;width:470px;font-size:12.3px;line-height:20px}
.about .copy p{margin-bottom:18px}
.about .copy strong{font-size:15px;font-weight:700}
.outline-btn{position:absolute;left:64px;top:396px;width:117px;height:35px;border:1.5px solid var(--white);font-size:12px;font-weight:700;display:flex;align-items:center;justify-content:center}

/* product arrows */
.arrows{left:1019px;top:1935px;display:flex;gap:8px}
.arrows span{width:28px;height:28px;border:1px solid var(--line);display:flex;align-items:center;justify-content:center}

/* cta band */
.cta{left:0;top:2369px;width:1200px;height:135px;background:var(--orange);color:var(--white)}
.cta .quote-label{position:absolute;left:106px;top:34px;font-size:28px;font-weight:600}
.cta .quote-phone{position:absolute;left:106px;top:70px;font-size:41px;font-weight:700;white-space:nowrap}
.cta .divider{position:absolute;left:423px;top:28px;width:1px;height:80px;background:rgba(255,255,255,.6)}
.cta .news-label{position:absolute;left:465px;top:30px;font-size:28px;font-weight:600}
.field{position:absolute;top:63px;height:46px;background:var(--white);color:#aaa;font-size:13.5px;display:flex;align-items:center;padding-left:14px}
.go{position:absolute;left:1036px;top:63px;width:56px;height:46px;background:var(--dark);color:var(--white);font-size:20px;font-weight:700;display:flex;align-items:center;justify-content:center}

/* footer */
.footer{left:0;top:2504px;width:1200px;height:336px;background:var(--dark);color:#ddd}
.fcol{position:absolute;top:56px}
.fcol h4{font-size:15px;font-weight:700;color:var(--white)}
.fcol .bar{width:38px;height:2px;background:var(--white);margin:12px 0 16px}
.fcol .intro{font-size:11.5px;color:#ddd}
.fcol ul{list-style:none;font-size:11.8px;line-height:25.5px}
.finput{width:196px;height:34px;background:var(--white);color:#aaa;font-size:12px;display:flex;align-items:center;padding-left:10px;margin-top:12px}
.signup{width:78px;height:36px;background:var(--orange);color:var(--white);font-size:13px;font-weight:700;display:flex;align-items:center;justify-content:center;margin-top:12px}
.contact-row{position:absolute;left:875px;display:flex;gap:14px}
.sq{width:38px;height:38px;border:1px solid #888;display:flex;align-items:center;justify-content:center;flex:none}
.contact-row .k{font-size:11.5px;font-weight:700;color:var(--white)}
.contact-row .v{font-size:11.8px;line-height:17px;color:#ddd;white-space:nowrap}
.footer .hr{position:absolute;left:875px;top:240px;width:232px;height:1px;background:#666}
.footer .social-row{position:absolute;left:875px;top:263px;display:flex;align-items:center;gap:14px;font-size:14px;font-weight:700;color:var(--white)}
.copyright{left:0;top:2840px;width:1200px;height:45px;background:var(--darker);color:#ddd;font-size:12px;display:flex;align-items:center;justify-content:center}
</style>
</head>
<body>
<div class="page">

  <div class="abs topbar">
    <div class="item" style="left:100px">
      <svg width="12" height="12" viewBox="0 0 24 24"><path fill="#f15a24" d="M6.6 10.8a15 15 0 0 0 6.6 6.6l2.2-2.2c.3-.3.7-.4 1-.2 1.1.4 2.3.6 3.6.6.6 0 1 .4 1 1V20c0 .6-.4 1-1 1A17 17 0 0 1 3 4c0-.6.4-1 1-1h3.5c.6 0 1 .4 1 1 0 1.3.2 2.5.6 3.6.1.3 0 .7-.2 1z"/></svg>
      Call Us : 1800 7 BRYND
    </div>
    <div class="item" style="left:270px">
      <svg width="13" height="10" viewBox="0 0 26 20"><rect x="1" y="1" width="24" height="18" fill="none" stroke="#f15a24" stroke-width="2"/><path d="M1 1l12 10L25 1" fill="none" stroke="#f15a24" stroke-width="2"/></svg>
      sales@quillmarkenergy.example.au
    </div>
    <div class="social">
      <span class="dot"></span><span class="dot"></span><span class="dot"></span><span class="dot"></span>
    </div>
  </div>

  <header class="abs header">
    <div class="brand"><span class="brand-mark"></span><span class="brand-name">Quillmark Energy</span></div>
    <div class="info" style="left:657px">
      <span class="ring"><svg width="14" height="18" viewBox="0 0 14 18"><path d="M7 1a6 6 0 0 1 6 6c0 4.5-6 10-6 10S1 11.5 1 7a6 6 0 0 1 6-6z" fill="none" stroke="#f15a24" stroke-width="1.5"/><circle cx="7" cy="7" r="2" fill="#f15a24"/></svg></span>
      <div><div class="label">Our Location</div><div class="value"><b>18</b> Harlow St, Melbourne 3000</div></div>
    </div>
    <div class="info" style="left:897px">
      <span class="ring"><svg width="16" height="16" viewBox="0 0 16 16"><circle cx="8" cy="8" r="6.5" fill="none" stroke="#f15a24" stroke-width="1.5"/><path d="M8 4v4l3 2" fill="none" stroke="#f15a24" stroke-width="1.5"/></svg></span>
      <div><div class="label">Working Hours</div><div class="value">Mon - Fri : 9:00 Am - 7:00 Pm</div></div>
    </div>
  </header>

  <nav class="abs nav">
    <ul><li>Home</li><li>About Us</li><li>Solutions</li><li>Products</li><li>Contact Us</li><li>Support</li><li>FAQ's</li><li>Blog</li></ul>
    <div class="quote-btn">GET A QUOTE</div>
  </nav>

  <section class="abs hero" role="img" aria-label="Technician in hard hat installing rows of solar panels on a commercial rooftop">
    <h1>WE MAKE SOLAR ENERGY WORK<br>FOR YOUR BUSINESS</h1>
    <div class="btn btn-primary">Get Appointment</div>
    <div class="btn btn-secondary">Contact Us</div>
  </section>

  <h2 class="abs section-title" style="top:748px">What We Do</h2>
  <div class="abs rule" style="top:781px"></div>
  <p class="abs section-lead" style="top:794px">We provide a professional renovation and installation services with a real focus on customer satisfaction.<br>Our installations are carried out by fully trained staff to the highest professional standards.</p>

  <article class="abs card" style="left:115px;top:867px;width:452px;height:366px">
    <div class="media" role="img" aria-label="Aerial view of solar panel arrays on residential rooftops" style="height:202px;background:linear-gradient(170deg,#8aa0b8,#3a4f8c 55%,#2c3d6e)"></div>
    <h3>Residential Solution</h3>
    <p>We provide a professional renovation and installation services with a real focus on customer satisfaction.</p>
    <span class="more">Read More</span>
  </article>
  <article class="abs card" style="left:629px;top:867px;width:452px;height:366px">
    <div class="media" role="img" aria-label="Installer fitting a solar panel on a tiled roof under blue sky" style="height:202px;background:linear-gradient(180deg,#2f7fc4,#5a9bd3 55%,#3b4a66)"></div>
    <h3>Commercial Solution</h3>
    <p>We provide a professional renovation and installation services with a real focus on customer satisfaction.</p>
    <span class="more">Read More</span>
  </article>

  <div class="abs about-media" role="img" aria-label="Engineer in hard hat giving thumbs up beside solar panels and a wind turbine"></div>
  <section class="abs about">
    <h2>ABOUT US</h2>
    <div class="copy">
      <p>Quillmark Energy is a national company that specialises in solar solutions for the commercial market. We also provide solutions for the residential market, bringing our uncompromising quality and service to the home.</p>
      <p>The founder of the company has over <strong>10 years experience</strong> delivering projects on both a residential and commercial scale, having overseen the installation of more than 3 megawatts of solar projects. They were a pioneer on the first megawatt scale project in Australia.</p>
      <p>As a leader in the field, we offer cutting edge solar technology backed by industry leading warranties. All our systems are designed and installed by Clear Power Board accredited persons. Our award winning designer will ensure your system will give the best long term performance and return on investment.</p>
    </div>
    <div class="outline-btn">READ MORE</div>
  </section>

  <h2 class="abs section-title" style="top:1862px">Our Products</h2>
  <div class="abs rule" style="top:1895px"></div>
  <p class="abs section-lead" style="top:1909px">We provide a professional renovation and installation services with a real focus on customer satisfaction.<br>Our installations are carried out by fully trained staff to the highest professional standards.</p>
  <div class="abs arrows">
    <span><svg width="8" height="12" viewBox="0 0 8 12"><path d="M6 1L1 6l5 5" fill="none" stroke="#999" stroke-width="1.5"/></svg></span>
    <span><svg width="8" height="12" viewBox="0 0 8 12"><path d="M2 1l5 5-5 5" fill="none" stroke="#999" stroke-width="1.5"/></svg></span>
  </div>

  <article class="abs card" style="left:115px;top:1983px;width:300px;height:319px">
    <div class="media" role="img" aria-label="Solar panels on a red tiled house roof" style="height:152px;background:linear-gradient(180deg,#2f86d6,#3b5fa0 50%,#b5522e 80%,#4f8a3a)"></div>
    <h3>Solar Panels</h3>
    <p style="width:270px">We provide a professional renovation and installation services with a real focus on customer satisfaction.</p>
    <span class="more">Read More</span>
  </article>
  <article class="abs card" style="left:450px;top:1983px;width:300px;height:319px">
    <div class="media" role="img" aria-label="Row of solar inverter units in front of a solar farm" style="height:152px;background:linear-gradient(180deg,#5d86b8,#2e3a4e 50%,#1e1e22 75%,#4d7d3a)"></div>
    <h3>Solar Inverters</h3>
    <p style="width:270px">We provide a professional renovation and installation services with a real focus on customer satisfaction.</p>
    <span class="more">Read More</span>
  </article>
  <article class="abs card" style="left:783px;top:1983px;width:300px;height:319px">
    <div class="media" role="img" aria-label="Operator at a wall of monitoring screens" style="height:152px;background:linear-gradient(160deg,#c9ced6,#6f7f92 50%,#3a4452)"></div>
    <h3>Monitoring Systems</h3>
    <p style="width:270px">We provide a professional renovation and installation services with a real focus on customer satisfaction.</p>
    <span class="more">Read More</span>
  </article>

  <section class="abs cta">
    <div class="quote-label">GET FREE QUOTE</div>
    <div class="quote-phone">1800 7 BRYND</div>
    <div class="divider"></div>
    <div class="news-label">SUBSCRIBE TO NEWSLETTER</div>
    <div class="field" style="left:467px;width:271px">Your Name</div>
    <div class="field" style="left:752px;width:273px">Type Your Email</div>
    <div class="go">GO</div>
  </section>

  <footer class="abs footer">
    <div class="fcol" style="left:104px">
      <h4>Quick Appointment</h4><div class="bar"></div>
      <div class="intro">Fill this form to get Quick appoitment.</div>
      <div class="finput">Your Name *</div>
      <div class="finput">Your Phone *</div>
      <div class="signup">SIGN UP</div>
    </div>
    <div class="fcol" style="left:360px">
      <h4>Services</h4><div class="bar"></div>
      <ul><li>Cosmetic Dentistry</li><li>Advanced Technology</li><li>Mini Planet</li><li>Preventive Dentistry</li><li>General Dentistry</li><li>Emergency Dentistry</li></ul>
    </div>
    <div class="fcol" style="left:617px">
      <h4>Office Hours</h4><div class="bar"></div>
      <ul style="line-height:30px"><li>Monday: 09:00 - 17:00</li><li>Tuesday: 09:00 - 17:00</li><li>Wednesday: 09:00 - 17:00</li><li>Thursday: 09:00 - 17:00</li><li>Friday: 09:00 - 17:00</li><li>Saturday, Sunday: By appointment only</li></ul>
    </div>

    <div class="contact-row" style="top:48px">
      <span class="sq"><svg width="16" height="14" viewBox="0 0 16 14"><path d="M8 1L1 7h2v6h4V9h2v4h4V7h2z" fill="#fff"/></svg></span>
      <div><div class="k">ADDRESS:</div><div class="v">18 Harlow Street<br>Suite 12 Melbourne VIC 3000</div></div>
    </div>
    <div class="contact-row" style="top:125px">
      <span class="sq"><svg width="10" height="16" viewBox="0 0 10 16"><rect x="1" y="1" width="8" height="14" rx="1.5" fill="none" stroke="#fff" stroke-width="1.5"/><circle cx="5" cy="12.5" r="1" fill="#fff"/></svg></span>
      <div><div class="k">PHONE:</div><div class="v">03-5550-1847, 1800-555-263</div></div>
    </div>
    <div class="contact-row" style="top:183px">
      <span class="sq"><svg width="16" height="12" viewBox="0 0 16 12"><rect x="0.5" y="0.5" width="15" height="11" fill="#fff"/><path d="M1 1l7 6 7-6" fill="none" stroke="#2b2b2b" stroke-width="1.3"/></svg></span>
      <div><div class="k">EMAIL:</div><div class="v">support@quillmarkenergy.example.au</div></div>
    </div>
    <div class="hr"></div>
    <div class="social-row">Social: <span class="dot"></span><span class="dot"></span><span class="dot"></span></div>
  </footer>

  <div class="abs copyright">Copyright © 2017 quillmarkenergy.example.au. All rights reserved.</div>
</div>
</body>
</html>
```